Gift Card Designs for different ocassions

We supply gift cards to retailers. Most use one design and we would like to offer them different card designs for different occasions. They would be Birthday, christmas, Fathers day, Mothers day. Others would be You Rock, You are a star, Thank You, Awesome stuff, My Hero, Great effort and congratulations.
We really want a fun, funky design that makes the gift card pop.

Target Market(s)

Anyone who buys a gift card

Colors

Designer to choose colors to be used in the design.

Requirements
Nice to have
• just need exciting , funky designs that stand out.
Should not have
• dull boring colours that make it look to corporate

```html
<!DOCTYPE html>
<html lang="en">
<head>
<meta charset="utf-8">
<title>Mother's Day Gift Card – Front and Back</title>
<link rel="stylesheet" href="https://fonts.googleapis.com/css2?family=Great+Vibes&family=Oswald:wght@500&display=swap">
<style>
  :root {
    --page-bg: #f4efec;
    --card-edge: #e48f7c;
    --card-rose: #e7a0b4;
    --card-cream: #f5ddd2;
    --card-blush: #f2c9c6;
    --lettering-rose: #cf6f7c;
    --lettering-shade: #7a3c45;
    --badge-plum: #6e3e44;
    --badge-text: #f6e4e4;
    --bloom-pink: #ec9fae;
    --bloom-leaf: #9cb98a;
    --stripe-black: #050505;
  }
  * { box-sizing: border-box; margin: 0; padding: 0; }
  html, body {
    width: 1200px;
    height: 800px;
    overflow: hidden;
    background: var(--page-bg);
  }
  .canvas { position: relative; width: 1200px; height: 800px; }

  .gift-card {
    position: absolute;
    width: 560px;
    height: 353px;
    border-radius: 18px;
    overflow: hidden;
    background:
      radial-gradient(ellipse 70% 65% at 55% 50%, var(--card-cream) 0%, rgba(245,221,210,0) 70%),
      radial-gradient(ellipse 60% 50% at 20% 95%, var(--card-rose) 0%, rgba(231,160,180,0) 70%),
      radial-gradient(ellipse 50% 40% at 80% 10%, var(--card-blush) 0%, rgba(242,201,198,0) 70%),
      var(--card-edge);
    box-shadow: 0 10px 24px rgba(80, 40, 40, 0.18);
  }
  .gift-card--front { left: 40px; top: 50px; }
  .gift-card--back  { left: 600px; top: 400px; }

  .greeting { position: absolute; inset: 0; color: var(--lettering-rose); }
  .greeting span {
    position: absolute;
    line-height: 1;
    white-space: nowrap;
    text-shadow: 2px 2px 0 var(--lettering-shade);
  }
  .greeting__happy {
    font-family: "Oswald", sans-serif;
    font-weight: 500;
    letter-spacing: 0.04em;
  }
  .greeting__mothers, .greeting__day {
    font-family: "Great Vibes", cursive;
    font-weight: 400;
  }

  .gift-card--front .greeting__happy   { left: 150px; top: 48px;  font-size: 40px; }
  .gift-card--front .greeting__mothers { left: 34px;  top: 70px;  font-size: 140px; }
  .gift-card--front .greeting__day     { left: 300px; top: 175px; font-size: 120px; }

  .gift-card--back .greeting span      { text-shadow: 1px 1px 0 var(--lettering-shade); }
  .gift-card--back .greeting__happy    { left: 352px; top: 128px; font-size: 17px; }
  .gift-card--back .greeting__mothers  { left: 330px; top: 134px; font-size: 62px; }
  .gift-card--back .greeting__day      { left: 440px; top: 178px; font-size: 52px; }

  .badge-bouquet {
    position: absolute;
    border-radius: 50%;
    background: radial-gradient(circle, var(--bloom-pink) 0%, var(--bloom-pink) 60%, var(--bloom-leaf) 85%, rgba(156,185,138,0) 100%);
    display: flex;
    align-items: center;
    justify-content: center;
  }
  .badge {
    border-radius: 50%;
    background: var(--badge-plum);
    display: flex;
    flex-direction: column;
    align-items: center;
    justify-content: center;
    color: var(--badge-text);
    font-family: "Great Vibes", cursive;
    font-weight: 400;
    line-height: 0.85;
  }
  .gift-card--front .badge-bouquet { left: 88px; top: 178px; width: 166px; height: 166px; }
  .gift-card--front .badge { width: 112px; height: 112px; font-size: 42px; }
  .gift-card--back  .badge-bouquet { left: 388px; top: 232px; width: 124px; height: 124px; }
  .gift-card--back  .badge { width: 86px; height: 86px; font-size: 32px; }

  .magnetic-stripe {
    position: absolute;
    left: 0;
    top: 42px;
    width: 100%;
    height: 64px;
    background: var(--stripe-black);
  }
</style>
</head>
<body>
  <main class="canvas">
    <section class="gift-card gift-card--front" aria-label="Gift card front">
      <h1 class="greeting">
        <span class="greeting__happy">HAPPY</span>
        <span class="greeting__mothers">Mother's</span>
        <span class="greeting__day">day</span>
      </h1>
      <div class="badge-bouquet" role="img" aria-label="Ring of watercolour roses and leaves around the badge">
        <p class="badge"><span>best</span><span>mom</span></p>
      </div>
    </section>

    <section class="gift-card gift-card--back" aria-label="Gift card back">
      <div class="magnetic-stripe"></div>
      <h2 class="greeting">
        <span class="greeting__happy">HAPPY</span>
        <span class="greeting__mothers">Mother's</span>
        <span class="greeting__day">day</span>
      </h2>
      <div class="badge-bouquet" role="img" aria-label="Ring of watercolour roses and leaves around the badge">
        <p class="badge"><span>best</span><span>mom</span></p>
      </div>
    </section>
  </main>
</body>
</html>
```